Accounting services

Looking for a Business card & Logo design

company name - LUMEN ACCOUNTING & TAXATION SOLUTIONS

name - Corwin Pell

position - Accountant / Business Consultant

email - "undecided"

Tel : (868) 512-4873 / (868) 587-2196

**PUT THESE TO THE BACK**
Accounting - VAT * INCOME/CORP TAX * RETURNS

REGISTRATION - VAT * NIS * Company Registration/Business Plan

Industry/Entity Type

Business

```html
<!DOCTYPE html>
<html lang="en">
<head>
<meta charset="UTF-8">
<title>Lumen Accounting &amp; Taxation Solutions — Business Card</title>
<link href="https://fonts.googleapis.com/css2?family=Arimo:wght@400;700&family=Exo+2:ital,wght@1,800&display=swap" rel="stylesheet">
<style>
  :root {
    --page-bg: #ffffff;
    --brand-blue: #3b95be;
    --bar-blue: #2f7fa6;
    --card-white: #fbfbfb;
    --ink: #1f1f1f;
    --ink-soft: #333333;
    --shadow: rgba(0, 0, 0, 0.22);
  }
  * { margin: 0; padding: 0; box-sizing: border-box; }
  html, body {
    width: 1200px;
    height: 520px;
    overflow: hidden;
    background: var(--page-bg);
  }
  .canvas {
    position: relative;
    width: 1200px;
    height: 520px;
  }
  .card {
    position: absolute;
    top: 94px;
    width: 580px;
    height: 332px;
    box-shadow: 2px 3px 6px var(--shadow);
    overflow: hidden;
  }

  /* Front */
  .card--front {
    left: 14px;
    background: var(--brand-blue);
  }
  .brand-mark {
    position: absolute;
    left: 226px;
    top: 68px;
    width: 128px;
    height: 108px;
  }
  .brand-mark__label {
    font-family: "Exo 2", sans-serif;
    font-weight: 800;
    font-style: italic;
    font-size: 20px;
    fill: var(--brand-blue);
  }
  .company-name {
    position: absolute;
    left: 0;
    right: 0;
    top: 200px;
    text-align: center;
    font-family: "Exo 2", sans-serif;
    font-weight: 800;
    font-style: italic;
    font-size: 25px;
    letter-spacing: 0.5px;
    color: #ffffff;
  }

  /* Back */
  .card--back {
    left: 603px;
    background: var(--card-white);
  }
  .name-bar {
    position: absolute;
    top: 46px;
    left: 0;
    right: 0;
    height: 22px;
    display: flex;
    align-items: center;
  }
  .name-bar__lead {
    width: 26px;
    height: 13px;
    background: var(--bar-blue);
  }
  .name-bar__name {
    padding: 0 5px 0 6px;
    font-family: "Arimo", sans-serif;
    font-weight: 700;
    font-size: 17px;
    color: var(--ink);
    white-space: nowrap;
  }
  .name-bar__rule {
    flex: 1;
    height: 13px;
    background: var(--bar-blue);
  }
  .job-title {
    position: absolute;
    top: 66px;
    left: 31px;
    font-family: "Arimo", sans-serif;
    font-size: 12.5px;
    color: var(--bar-blue);
  }
  .services {
    list-style: none;
    font-family: "Arimo", sans-serif;
    font-size: 16px;
    color: var(--ink);
  }
  .services__item {
    position: absolute;
    left: 31px;
    display: flex;
    align-items: center;
    white-space: nowrap;
  }
  .services__bullet {
    width: 9px;
    height: 9px;
    margin-right: 7px;
    flex: none;
  }
  .contact {
    position: absolute;
    top: 142px;
    right: 42px;
    font-family: "Arimo", sans-serif;
    font-size: 17px;
    color: var(--ink-soft);
    line-height: 22px;
  }
  .contact__row {
    display: flex;
    justify-content: flex-end;
  }
  .contact__label {
    font-weight: 700;
    color: var(--bar-blue);
    margin-right: 6px;
  }
</style>
</head>
<body>
<main class="canvas">

  <section class="card card--front" aria-label="Card front">
    <svg class="brand-mark" viewBox="0 0 128 108" aria-label="Lumen mark">
      <circle cx="64" cy="54" r="52" fill="#ffffff"/>
      <text class="brand-mark__label" x="64" y="61" text-anchor="middle">LUMEN</text>
    </svg>
    <h1 class="company-name">Lumen Accounting &amp; Taxation Solutions</h1>
  </section>

  <section class="card card--back" aria-label="Card back">
    <div class="name-bar">
      <span class="name-bar__lead"></span>
      <h2 class="name-bar__name">Corwin Pell</h2>
      <span class="name-bar__rule"></span>
    </div>
    <p class="job-title">Accountant / Business Consultant</p>

    <ul class="services">
      <li class="services__item" style="top:143px">
        <svg class="services__bullet" viewBox="0 0 10 10"><circle cx="5" cy="5" r="4.5" fill="#2f7fa6"/><circle cx="4" cy="4" r="1.6" fill="#ffffff" opacity="0.6"/></svg>Accounting - Vat</li>
      <li class="services__item" style="top:166px">
        <svg class="services__bullet" viewBox="0 0 10 10"><circle cx="5" cy="5" r="4.5" fill="#2f7fa6"/><circle cx="4" cy="4" r="1.6" fill="#ffffff" opacity="0.6"/></svg>Income / Corp Tax</li>
      <li class="services__item" style="top:187px">
        <svg class="services__bullet" viewBox="0 0 10 10"><circle cx="5" cy="5" r="4.5" fill="#2f7fa6"/><circle cx="4" cy="4" r="1.6" fill="#ffffff" opacity="0.6"/></svg>Returns</li>
      <li class="services__item" style="top:215px">
        <svg class="services__bullet" viewBox="0 0 10 10"><circle cx="5" cy="5" r="4.5" fill="#2f7fa6"/><circle cx="4" cy="4" r="1.6" fill="#ffffff" opacity="0.6"/></svg>Registration - Vat</li>
      <li class="services__item" style="top:241px">
        <svg class="services__bullet" viewBox="0 0 10 10"><circle cx="5" cy="5" r="4.5" fill="#2f7fa6"/><circle cx="4" cy="4" r="1.6" fill="#ffffff" opacity="0.6"/></svg>Nis</li>
      <li class="services__item" style="top:264px">
        <svg class="services__bullet" viewBox="0 0 10 10"><circle cx="5" cy="5" r="4.5" fill="#2f7fa6"/><circle cx="4" cy="4" r="1.6" fill="#ffffff" opacity="0.6"/></svg>Company Registration / Business Plan</li>
    </ul>

    <div class="contact">
      <p class="contact__row"><span class="contact__label">Tel :</span>(868) 512-4873</p>
      <p class="contact__row">(868) 587-2196</p>
    </div>
  </section>

</main>
</body>
</html>
```